Qdo me indicaram vcs me falaram q vcs são ótimos. Concordo e digo ainda mais...amei o atendimento, a atenção e a paciência. recomendo e tenho certeza q faremos mais projetos juntos.

```html
<!DOCTYPE html>
<html lang="pt-BR">
<head>
<meta charset="UTF-8">
<title>Doce das Primas — Cartão de visita</title>
<link rel="stylesheet" href="https://fonts.googleapis.com/css2?family=Cormorant+Garamond:wght@500&family=Montserrat:wght@400&display=swap">
<style>
  :root {
    --backdrop: #e6e6e9;
    --card-white: #ffffff;
    --wine: #561a2f;
    --wine-deep: #46142a;
    --gold: #c09066;
    --gold-light: #e3c09b;
    --ink-soft: #e9d6dc;
  }
  * { box-sizing: border-box; margin: 0; padding: 0; }
  html, body {
    width: 1200px; height: 1200px; overflow: hidden;
    background: var(--backdrop);
  }
  .sheet {
    position: relative; width: 1200px; height: 1200px;
    display: flex; flex-direction: column; align-items: center; justify-content: center; gap: 60px;
  }
  .card {
    position: relative; width: 900px; height: 500px; overflow: hidden;
    box-shadow: 0 12px 30px rgba(0,0,0,.12);
  }
  .card--front { background: var(--card-white); }
  .card--back { background: var(--wine); }

  .brand-name {
    font-family: "Cormorant Garamond", serif;
    font-weight: 500;
    color: var(--gold);
    letter-spacing: 2px;
    white-space: nowrap;
  }
  .card--front .brand-name {
    position: absolute; right: 80px; top: 50%; transform: translateY(-50%);
    font-size: 56px;
  }

  .back-band {
    position: absolute; left: 0; top: 0; width: 100%; height: 150px;
    background: var(--wine-deep);
  }
  .card--back .brand-name {
    position: absolute; left: 50%; top: 190px; transform: translateX(-50%);
    font-size: 62px; color: var(--gold-light);
  }
  .gold-edge {
    position: absolute; left: 0; bottom: 0; width: 100%; height: 8px;
    background: linear-gradient(90deg, var(--gold), var(--gold-light), var(--gold));
  }

  .contact {
    position: absolute; left: 60px; right: 60px; bottom: 50px;
    display: flex; justify-content: space-between; align-items: flex-start;
    font-family: "Montserrat", sans-serif; font-size: 15px; line-height: 1.7;
    color: var(--ink-soft);
  }
  .contact-group { display: flex; flex-direction: column; }
  .contact-line { display: flex; align-items: center; gap: 10px; }
  .contact-line svg { width: 15px; height: 15px; flex: none; }
  .contact-line .icon-gap { width: 15px; flex: none; }
</style>
</head>
<body>
<main class="sheet">
  <section class="card card--front">
    <div class="brand-name">Doce das Primas</div>
  </section>

  <section class="card card--back">
    <div class="back-band"></div>
    <div class="brand-name">Doce das Primas</div>

    <div class="contact">
      <div class="contact-group">
        <div class="contact-line">
          <svg viewBox="0 0 16 16"><path d="M8 1a5 5 0 0 0-5 5c0 4 5 9 5 9s5-5 5-9a5 5 0 0 0-5-5zm0 7a2 2 0 1 1 0-4 2 2 0 0 1 0 4z" fill="var(--gold)"/></svg>
          <span>R. das Amoras, nº 12, Vila Nova - SP</span>
        </div>
        <div class="contact-line"><span class="icon-gap"></span><span>CEP 01234-000</span></div>
      </div>

      <div class="contact-group">
        <div class="contact-line">
          <svg viewBox="0 0 16 16"><rect x="1" y="3" width="14" height="10" rx="1" fill="var(--gold)"/><path d="M1.5 3.5 8 9l6.5-5.5" stroke="var(--wine)" stroke-width="1.3" fill="none"/></svg>
          <span>contato@docedasprimas.com.br</span>
        </div>
        <div class="contact-line">
          <svg viewBox="0 0 16 16"><circle cx="8" cy="8" r="6.5" fill="none" stroke="var(--gold)" stroke-width="1.4"/><ellipse cx="8" cy="8" rx="2.6" ry="6.5" fill="none" stroke="var(--gold)" stroke-width="1.2"/><path d="M1.5 8h13" stroke="var(--gold)" stroke-width="1.2"/></svg>
          <span>www.docedasprimas.com.br</span>
        </div>
      </div>

      <div class="contact-group">
        <div class="contact-line">
          <svg viewBox="0 0 16 16"><path d="M4 1.5 6.2 4 5 5.8c.8 2 2.6 3.8 4.6 4.6L11.4 9l2.6 2.2-1.3 2.6C7.5 14 2 8.5 2.2 3.3z" fill="var(--gold)"/></svg>
          <span>(11) 95555-1234</span>
        </div>
        <div class="contact-line">
          <svg viewBox="0 0 16 16"><path d="M4 1.5 6.2 4 5 5.8c.8 2 2.6 3.8 4.6 4.6L11.4 9l2.6 2.2-1.3 2.6C7.5 14 2 8.5 2.2 3.3z" fill="var(--gold)"/></svg>
          <span>(11) 3333-4321</span>
        </div>
      </div>
    </div>

    <div class="gold-edge"></div>
  </section>
</main>
</body>
</html>
```